Starter & Alternator business needs a website

update: very good designs submitted so far. also need this to display well on mobile devices. not sure if wordpress or html/css is better for my needs.

Our existing website is vexlandrib.com and is need of total revamp. Need full design of a website for my business.

We sell and rebuild starters and alternators. Customers bring in the units and we rebuild them. Or we sell them brand new or rebuilt units we have in stock. We do not install units into vehicles like a mechanic would. We strictly rebuild starters and alternators in our shop, sell brand new units over the counter, and we do deliver occasionally as well. We do offer a line of Morlin batteries as well but that is only a small feature of the business.

I would like this website designed and coded. I can upload the files to my web host after completion. I can also add in and modify content like our background info, etc.

I have included an illustrator file that shows some of our signage and logo, etc. I have also included a radio commercial sample so you can get a little better feel for the business. A similar ad does run on the radio currently, slightly different and without the added sound effects.

Update: I do like using photos of real items(starters or alternators etc) for an icon, like a real alternator stock image for the alternator section icon, etc. Maybe incorporate our logo in that design as well. That looks nice as well and may aid in navigation.

For any other design elements, do what you think looks good. Our colors are red/white/blue as seen in the illustrator file. our building is painted with talbot greaves colors, emberglow red and deep harbor for blue.

Here are some examples of rebuilders websites in other markets for reference:

https://brommelgarage.com/starter-alternator-rebuilding/

https://www.quintonmotorworks.com/auto-repairs/alternator-starter-rebuilds.aspx

https://www.lorvexcharging.com/

https://www.damblingwx.com/

The website can have areas for: services and products offered, high output alternators, Morlin Batteries, troubleshooting tips, current specials, contact info and directions/map, etc. Whatever else you feel applies.

At some point I do want to be able to sell items directly online or at least have a secure section for customers to submit invoice payments, but that's not necessarily in scope for this project just something to keep in mind.

Target Market(s)

Mechanics and Managers in fleet shops, construction and marine industries, shipping trades. Also automobile owners who work on their own vehicles. We sell and rebuild starters and alternators for automobiles, heavy duty equipment, forklifts, gradalls, man movers, bobcats, loaders, large tractors and trucks, just about any engine, golf carts, generators, etc.

Industry/Entity Type

Automotive Part

Coding

Coded - Design and coding required

Number of Pages Required

5+ page

Font styles to use
Serif
Sans Serif

Colors
0255a3
ec1f27
ffffff

Requirements
Must have
• Should also display nicely on mobile phones. Highlight our specialty, "Starters & Alternators"

```html
<!DOCTYPE html>
<html lang="en">
<head>
<meta charset="utf-8">
<title>Harborline Rebuilders – Services</title>
<link href="https://fonts.googleapis.com/css2?family=Fira+Sans:wght@400;500;600;700&family=Ubuntu:wght@700&display=swap" rel="stylesheet">
<style>
:root{
  --red:#ec1f27;
  --blue:#0255a3;
  --navy:#183463;
  --deep-red:#a61e22;
  --btn-red:#9e1218;
  --white:#ffffff;
  --grey:#eef0f0;
}
*{margin:0;padding:0;box-sizing:border-box}
html,body{width:863px;height:1200px;overflow:hidden}
body{position:relative;background:var(--white);font-family:"Fira Sans",sans-serif;color:var(--navy)}
.abs{position:absolute}

.topbar{left:0;top:0;width:863px;height:33px;background:var(--red);color:var(--white);font-size:11px;font-weight:600}
.topbar .contact{left:12px;top:9px;display:flex;gap:8px;align-items:center}
.topbar .contact span{display:flex;align-items:center;gap:3px}
.topbar .hours{right:12px;top:9px;display:flex;gap:8px;align-items:center}

.header{left:0;top:33px;width:863px;height:89px}
.brand{left:46px;top:24px;display:flex;align-items:center;gap:6px;color:var(--navy);font-weight:700;font-size:12px;line-height:1.15;width:110px}
.brand .dot{width:14px;height:14px;border-radius:50%;background:var(--red);flex:none}
.nav{left:247px;top:38px;display:flex;gap:0;font-size:11.5px;font-weight:600;color:var(--blue)}
.nav a{color:inherit;text-decoration:none;margin-right:23px}
.nav a.active{color:var(--red)}

.banner{left:0;top:122px;width:863px;height:85px;background:var(--red);display:flex;align-items:center;justify-content:center}
.banner h1{color:var(--white);font-size:15px;font-weight:600;text-decoration:underline;text-underline-offset:3px}

.card{top:265px;width:260px;height:275px;border:1.5px solid var(--red);border-radius:4px;overflow:hidden;background:var(--white)}
.card .photo{height:197px;margin:10px 14px 0}
.card .label{position:absolute;left:0;bottom:0;width:100%;height:76px;background:var(--grey);display:flex;align-items:center;justify-content:center;text-align:center;color:var(--red);font-size:18px;font-weight:600;line-height:1.1}
.photo.starter{background:radial-gradient(ellipse at 55% 45%,#3a3f4a 0%,#1f232b 50%,#ffffff 75%)}
.photo.alt{background:radial-gradient(ellipse at 50% 50%,#c9c4bb 0%,#8e8a83 45%,#ffffff 72%)}
.photo.new{background:radial-gradient(ellipse at 55% 45%,#2b2e35 0%,#8a8c8e 48%,#ffffff 72%)}

.feature-mark{left:95px;top:594px;width:134px;height:140px;display:flex;flex-direction:column;align-items:center;justify-content:center;gap:8px}
.feature-mark .dot{width:60px;height:60px;border-radius:50%;background:var(--red)}
.feature-mark .name{font-size:13px;font-weight:700;color:var(--navy);text-align:center;line-height:1.15}
.specialty{left:238px;top:592px;width:492px;font-family:"Ubuntu",sans-serif;font-weight:700;color:var(--navy);line-height:.95}
.specialty .l1{display:block;font-size:64px;padding-left:45px}
.specialty .l1 small{font-size:46px}
.specialty .l2{display:block;font-size:67px;margin-top:4px}
.phone-line{left:97px;top:750px;width:632px;height:60px;display:flex;align-items:center;justify-content:space-between}
.phone-line .rule{width:154px;height:3px;background:var(--deep-red)}
.phone-line .num{font-family:"Ubuntu",sans-serif;font-weight:700;font-size:62px;color:var(--deep-red);letter-spacing:1px}
.tagline{left:97px;top:836px;width:632px;display:flex;align-items:center;font-size:22px;font-weight:700;color:var(--navy);white-space:nowrap}
.tagline .bolt{margin:0 4px}
.tagline .addr{margin-left:auto}
.queries{left:0;top:892px;width:830px;text-align:center;font-size:14.5px;font-weight:600;color:var(--navy);text-decoration:underline;text-underline-offset:2px}

.footer{left:0;top:947px;width:863px;height:253px;background:var(--red);color:var(--white)}
.footer h2{position:absolute;font-size:14.5px;font-weight:600;white-space:nowrap}
.footer h2::after{content:"";position:absolute;left:0;right:0;bottom:-5px;height:2px;background:var(--white)}
.overview{left:24px;top:60px;width:162px;font-size:10px;line-height:15.2px;text-align:justify}
.links{list-style:none;font-size:10.5px;line-height:15.2px}
.links li::before{content:"* ";margin-right:4px}
.form{left:651px;top:62px;width:174px}
.form .field{height:19px;background:var(--white);border-radius:5px;margin-bottom:4.5px;color:var(--red);font-size:10.5px;padding:2px 12px;line-height:15px}
.form .field.msg{height:40px}
.form .btns{display:flex;gap:5px;justify-content:center;margin-top:5px}
.form .btn{width:75px;height:17px;background:var(--btn-red);border-radius:5px;font-size:10.5px;text-align:center;line-height:17px}
.copy{left:0;top:240px;width:863px;text-align:center;font-size:6.5px}
</style>
</head>
<body>

<div class="topbar abs">
  <div class="contact abs">
    <span><svg width="8" height="11" viewBox="0 0 8 11"><path d="M4 0a4 4 0 0 0-4 4c0 3 4 7 4 7s4-4 4-7a4 4 0 0 0-4-4zm0 5.5a1.5 1.5 0 1 1 0-3 1.5 1.5 0 0 1 0 3z" fill="#fff"/></svg>4417 Waialoa St, Honolulu, HI</span>
    <span><svg width="11" height="9" viewBox="0 0 11 9"><path d="M1 3c0-2 9-2 9 0v1H8V3H3v1H1zM2.5 5h6l1 3.5h-8z" fill="none" stroke="#fff" stroke-width="1"/></svg>808-555-0142</span>
    <span><svg width="11" height="8" viewBox="0 0 11 8"><rect width="11" height="8" fill="#fff"/><path d="M0 0l5.5 4.5L11 0" fill="none" stroke="#ec1f27"/></svg>INFO@vexlandrib.com</span>
  </div>
  <div class="hours abs">
    <svg width="13" height="12" viewBox="0 0 13 12"><rect x="1" y="2" width="10" height="9" fill="none" stroke="#fff"/><path d="M1 4.5h10M3.5 0.5v3M8.5 0.5v3" stroke="#fff"/></svg>
    <span>MON - FRI&nbsp; 10:30 A.M&nbsp; To 7:00 P.M</span>
  </div>
</div>

<header class="header abs">
  <div class="brand abs"><span class="dot"></span><span>HARBORLINE REBUILDERS</span></div>
  <nav class="nav abs">
    <a href="#">HOME</a><a href="#">ABOUT US</a><a href="#" class="active">SERVICES</a><a href="#">PRODUCTS</a><a href="#">TROUBLESHOOTING TIPS</a><a href="#">BLOG</a><a href="#">CONTACT US</a>
  </nav>
</header>

<section class="banner abs"><h1>OUR OFFERED SERVICES</h1></section>

<article class="card abs" style="left:15px">
  <div class="photo starter" role="img" aria-label="Product photo of a black starter motor"></div>
  <div class="label">REBUILD STARTERS</div>
</article>
<article class="card abs" style="left:301px">
  <div class="photo alt" role="img" aria-label="Product photo of a silver alternator"></div>
  <div class="label">REBUILD ALTERNATORS</div>
</article>
<article class="card abs" style="left:582px">
  <div class="photo new" role="img" aria-label="Product photo of a new starter generator"></div>
  <div class="label">BUY BRAND NEW<br>STARTERS &amp; ALTERNATORS</div>
</article>

<div class="feature-mark abs"><span class="dot"></span><span class="name">HARBORLINE<br>REBUILDERS</span></div>
<h2 class="specialty abs"><span class="l1">STARTERS <small>&amp;</small></span><span class="l2">ALTERNATORS</span></h2>
<div class="phone-line abs"><span class="rule"></span><span class="num">555-0142</span><span class="rule"></span></div>
<div class="tagline abs">
  Automotive<svg class="bolt" width="12" height="24" viewBox="0 0 12 24"><path d="M8 0L2 13h4L3 24l9-14H7l4-10z" fill="#a61e22"/></svg>Marine<svg class="bolt" width="12" height="24" viewBox="0 0 12 24"><path d="M8 0L2 13h4L3 24l9-14H7l4-10z" fill="#a61e22"/></svg>Heavy Duty
  <span class="addr">4417 Waialoa St</span>
</div>
<p class="queries abs">CONTACT US AT THE ABOVE NO FOR ANY QUERIES</p>

<footer class="footer abs">
  <h2 style="left:44px;top:25px">OUR OVERVIEW</h2>
  <p class="overview abs">Lorem ipsum dolor sit amet, no nam quem atqui scriptorem, eum munere prodesset id, ut audiam vivendum evertitur pro. Id hinc duis equidem vix. Pri vidit munere ut, sea duis justo percipit at. Tantas melius omnium eam ex. No vix meliore ponderum rationibus, dolorum offendit appareat sit eu, vix et diam latine.</p>

  <h2 style="left:231px;top:25px">SERVICES WE OFFERED</h2>
  <ul class="links abs" style="left:219px;top:61px">
    <li>REBUILD STARTERS</li><li>REBUILD ALTERNATORS</li><li>SELLING BRAND NEW STARTERS</li><li>SELLING BRAND NEW ALTERNATORS</li>
  </ul>

  <h2 style="left:466px;top:23px">QUICK LINKS</h2>
  <ul class="links abs" style="left:450px;top:61px">
    <li>HOME</li><li>ABOUT US</li><li>SERVICES WE OFFERED</li><li>PRODUCTS WE SELL</li><li>CONTACT US</li>
  </ul>

  <h2 style="left:662px;top:19px">QUICK CONTACT</h2>
  <div class="form abs">
    <div class="field">Enter Your Name Here</div>
    <div class="field">Enter Your Email ID Here</div>
    <div class="field">Enter Your Phone Here</div>
    <div class="field">Enter Your Address Here</div>
    <div class="field msg">Your Message Here</div>
    <div class="btns"><span class="btn">SUBMIT</span><span class="btn">RESET</span></div>
  </div>

  <p class="copy abs">Copyright © 2019 Harborline Rebuilders</p>
</footer>

</body>
</html>
```